Benefit Card for new Customers - LUMIRO

We are planning our offline referral marketing programm. So we need a benefit card for new customers. We are a company that provides innovative and highly competent private tutoring for our customers. We are LUMIRO (www.lumiro-lernhilfe.ch) and are located in Bern (Switzerland). Our customers are schoolkids (and their parents), apprentices and students. Therefore we designed our corporate design for this target groups. Our corporate design is colourful (we use especially our corporate colours) and has as little edges as possible. As an illustration take a look at our website www.lumiro-lernhilfe.ch where we tried to realize our corporate identity as suitable as possible.
We would like to see designs that use our corporate colours (green, blue and tourquois might be inviting colours). The final design should be inviting for new customers, highly professional and not too overloaded.

Dimensions of the card: 148 x 105 mm (millimeter) --> A6 Format
Font: Lato

Upload Files:
- Corporate colour codes
- rough draft of the benefit card
- text and wording document
- Logo

Target Market(s)

Schoolkids (and their parents), apprentices, students

Industry/Entity Type

Education

Requirements
Must have
• Clean Design, Font: Lato, right Dimension as mentioned in the despriction,
Should not have
• Edges

```html
<!DOCTYPE html>
<html lang="de">
<head>
<meta charset="utf-8">
<title>LUMIRO Vorteils-Pass</title>
<link rel="stylesheet" href="https://fonts.googleapis.com/css2?family=Lato:wght@400;700;900&display=swap">
<style>
  :root {
    --mint: #4fd6b0;
    --sun: #f8c433;
    --sky: #5bb8e4;
    --orange: #ec8c3a;
    --ink: #222326;
    --rule: #8f8f8f;
    --paper: #ffffff;
    --backdrop: #ffffff;
  }
  * { box-sizing: border-box; margin: 0; padding: 0; }
  html, body {
    width: 1200px; height: 1200px; overflow: hidden;
    background: var(--backdrop);
    font-family: "Lato", sans-serif; color: var(--ink);
  }
  .card {
    position: absolute; left: 116px; top: 257px;
    width: 968px; height: 686px;
    background: var(--paper); overflow: hidden;
  }
  .band-top, .band-bottom { position: absolute; left: 0; width: 968px; }
  .band-top { top: 0; height: 110px; }
  .band-bottom { top: 600px; height: 86px; }

  .brand { position: absolute; left: 30px; top: 68px; width: 150px; text-align: center; }
  .brand-dot {
    width: 76px; height: 76px; border-radius: 50%;
    background: var(--mint); margin: 0 auto 14px;
  }
  .brand-name { font-size: 32px; font-weight: 700; letter-spacing: 5px; color: var(--ink); }

  .title {
    position: absolute; left: 268px; top: 122px;
    font-size: 27px; font-weight: 700; line-height: 36px;
  }
  .pass-no-line {
    position: absolute; left: 502px; top: 186px; width: 424px;
    border-top: 2px solid var(--rule);
  }

  .message {
    position: absolute; left: 34px; top: 232px; width: 892px;
    font-size: 19.5px; line-height: 34.6px; text-align: justify;
  }
  .message strong { font-weight: 900; }
  .cta {
    position: absolute; left: 34px; top: 382px;
    font-size: 22px; font-weight: 700; color: var(--orange);
  }

  .field { position: absolute; font-size: 22px; font-weight: 700; color: var(--sky); }
  .field-line { position: absolute; border-top: 2px solid var(--rule); }

  .option { position: absolute; font-size: 17.5px; display: flex; align-items: center; gap: 10px; }
  .checkbox {
    width: 20px; height: 18px; border: 2px solid var(--sky); border-radius: 2px;
  }
  .tick { width: 20px; height: 20px; }

  .more-info { position: absolute; left: 35px; top: 574px; font-size: 21px; }

  .contact {
    position: absolute; top: 640px; display: flex; align-items: center; gap: 10px;
    color: var(--paper); font-size: 23px; font-weight: 700;
  }
  .contact svg { width: 24px; height: 24px; }
</style>
</head>
<body>
<div class="card">
  <svg class="band-top" viewBox="0 0 968 110" aria-hidden="true">
    <path d="M0 0 H968 V74 H520 C480 74 468 60 456 46 C442 32 428 26 400 26 H0 Z" fill="var(--mint)"/>
    <path d="M0 28 H400 C428 28 442 34 456 48 C468 62 480 76 520 76 H968" fill="none" stroke="var(--sun)" stroke-width="4"/>
    <path d="M0 33 H400 C425 33 438 39 452 53 C465 67 478 82 520 82 H968" fill="none" stroke="var(--sky)" stroke-width="4"/>
  </svg>

  <div class="brand">
    <div class="brand-dot"></div>
    <div class="brand-name">LUMIRO</div>
  </div>

  <h1 class="title">Dein Vorteils-Pass<br>Vorteils-Pass-Nr.</h1>
  <div class="pass-no-line"></div>

  <p class="message">Hallo,<br>ich bin ein LUMIRO-Fan. Durch den innovativen und persönlichen Unterricht bei LUMIRO habe ich vieles gelernt und meine Noten markant gesteigert. Profitiere auch Du von LUMIRO. <strong>Mit diesem Vorteils-Pass schenken wir Dir eine Unterrichtslektion.</strong></p>
  <p class="cta">Melde Dich bei uns und lass Dich kostenlos und unverbindlich beraten.</p>

  <span class="field" style="left:32px; top:448px;">Empfohlen von</span>
  <div class="field-line" style="left:197px; top:471px; width:344px;"></div>
  <span class="field" style="left:32px; top:507px;">Freund</span>
  <div class="field-line" style="left:116px; top:529px; width:426px;"></div>

  <div class="option" style="left:575px; top:460px;">Gratislektion <span class="checkbox"></span></div>
  <div class="option" style="left:733px; top:460px;">Oder&nbsp; Kinogutschein <span class="checkbox" style="margin-left:6px;"></span></div>
  <div class="option" style="left:575px; top:517px;">Gratislektion ab 4 gebuchten
    <svg class="tick" viewBox="0 0 20 20" aria-hidden="true"><circle cx="10" cy="10" r="8.5" fill="none" stroke="var(--sky)" stroke-width="1.6"/><path d="M6 10.3 L9 13 L14 7.5" fill="none" stroke="var(--sky)" stroke-width="1.6" stroke-linecap="round" stroke-linejoin="round"/></svg>
  </div>

  <p class="more-info">weitere Infos unter www.lumiro-lernhilfe.ch/freundschaft/</p>

  <svg class="band-bottom" viewBox="0 0 968 86" aria-hidden="true">
    <path d="M0 12 H870 C915 12 945 26 968 48 V86 H0 Z" fill="var(--mint)"/>
    <path d="M0 13 H870 C915 13 945 27 968 48" fill="none" stroke="var(--sun)" stroke-width="4"/>
    <path d="M0 6 H875 C920 6 948 20 968 38" fill="none" stroke="var(--sky)" stroke-width="5"/>
  </svg>

  <div class="contact" style="left:34px;">
    <svg viewBox="0 0 24 24" aria-hidden="true"><rect width="24" height="24" rx="4" fill="var(--paper)"/><path d="M8 5 L10.5 8.5 L9 10.5 C10 12.5 11.5 14 13.5 15 L15.5 13.5 L19 16 L17.5 19 C11 19 5 13 5 6.5 Z" fill="var(--mint)"/></svg>
    076 000 12 34
  </div>
  <div class="contact" style="left:347px;">
    <svg viewBox="0 0 24 24" aria-hidden="true"><rect width="24" height="24" rx="4" fill="var(--paper)"/><rect x="5" y="7" width="14" height="10" rx="1.5" fill="var(--mint)"/><path d="M5.5 8 L12 13 L18.5 8" fill="none" stroke="var(--paper)" stroke-width="1.5"/></svg>
    hallo@lumiro-lernhilfe.ch
  </div>
  <div class="contact" style="left:676px;">
    <svg viewBox="0 0 24 24" aria-hidden="true"><rect width="24" height="24" rx="6" fill="var(--paper)"/><g fill="none" stroke="var(--mint)" stroke-width="1.4"><circle cx="12" cy="12" r="7"/><ellipse cx="12" cy="12" rx="3" ry="7"/><path d="M5 12 H19 M6 8.5 H18 M6 15.5 H18"/></g></svg>
    www.lumiro-lernhilfe.ch
  </div>
</div>
</body>
</html>
```